Mortgage Broking boutique Business

I’m wanting a revamped look to my existing business card design. I do like the black and silver but happy to have other colours introduced based on your creation. I’ve attached a copy of my current card so you can have a starting point updated details noted brloe. I deal with high net worth individuals so need my card to be sophisticated, classy that gives off a classy vibe

Target Market(s)

High net worth, wealthy

Industry/Entity Type

Mortgage Brokerage

Contact Information for Business Card

Job title: Finance Executive
Phone: +61 7 3287 4419
Mobile: 0471 352 608
Email: marcus@quillbrookcapital.com.au
Web: www.quillbrookcapital.com.au
Address: level 36 Tindale Court, 58 Harwick St Brisbane QLD 4000

Font styles to use
Other font styles liked:
• Helvetica

Colors

Designer to choose colors to be used in the design.

Requirements
Must have
• Use my existing card design as a starting point

```html
<!DOCTYPE html>
<html lang="en">
<head>
<meta charset="utf-8">
<title>Quillbrook Capital – Business Card</title>
<link rel="stylesheet" href="https://fonts.googleapis.com/css2?family=Arimo:wght@400;700&display=swap">
<style>
  :root {
    --backdrop: #2b2b2b;
    --card: #1f1f1f;
    --ink: #f2f2f2;
    --ink-soft: #d6d6d6;
    --silver: #c4c4c4;
    --foil-light: #e9e9e9;
    --foil-mid: #a9a9a9;
    --foil-dark: #7d7d7d;
  }
  * { box-sizing: border-box; margin: 0; padding: 0; }
  html, body { width: 1200px; height: 895px; overflow: hidden; }
  body {
    background: var(--backdrop);
    font-family: "Arimo", Helvetica, Arial, sans-serif;
    color: var(--ink);
    position: relative;
  }
  .card {
    position: absolute;
    left: 240px;
    width: 720px;
    height: 400px;
    background: var(--card);
    overflow: hidden;
    box-shadow: 0 10px 30px rgba(0,0,0,.45);
  }
  .card--front { top: 30px; }
  .card--back { top: 465px; }
  .foil-stripe {
    position: absolute;
    left: 0; right: 0; bottom: 0;
    height: 9px;
    background: linear-gradient(90deg, var(--foil-mid), var(--foil-light) 30%, var(--foil-dark) 55%, var(--foil-light) 80%, var(--foil-mid));
  }
  .brand {
    position: absolute;
    left: 0; right: 0; top: 130px;
    text-align: center;
    color: var(--silver);
    font-weight: 700;
    font-size: 38px;
    letter-spacing: 12px;
    line-height: 1.25;
    text-transform: uppercase;
  }
  .identity {
    position: absolute;
    right: 440px;
    top: 128px;
    text-align: right;
  }
  .identity__name {
    font-weight: 700;
    font-size: 40px;
    letter-spacing: 0.5px;
    text-transform: uppercase;
    color: var(--ink);
  }
  .identity__title {
    font-size: 17px;
    color: var(--ink-soft);
    margin-top: 2px;
  }
  .divider {
    position: absolute;
    left: 300px;
    top: 110px;
    width: 1.5px;
    height: 120px;
    background: var(--ink-soft);
  }
  .contacts {
    position: absolute;
    left: 322px;
    top: 112px;
    list-style: none;
  }
  .contacts li {
    display: flex;
    align-items: center;
    gap: 12px;
    font-size: 17px;
    line-height: 29px;
    color: var(--ink);
  }
  .contacts svg {
    width: 14px; height: 14px;
    fill: none;
    stroke: var(--ink);
    stroke-width: 1.6;
    flex: none;
  }
  .address {
    position: absolute;
    left: 40px;
    bottom: 36px;
    font-size: 17px;
    color: var(--ink);
  }
</style>
</head>
<body>
  <section class="card card--front">
    <h1 class="brand">Quillbrook<br>Capital</h1>
    <div class="foil-stripe"></div>
  </section>

  <section class="card card--back">
    <div class="identity">
      <p class="identity__name">Marcus Hale</p>
      <p class="identity__title">Finance Executive</p>
    </div>
    <div class="divider"></div>
    <ul class="contacts">
      <li>
        <svg viewBox="0 0 16 16" aria-hidden="true"><path d="M3 2l3 1 1 3-2 1.5a8 8 0 0 0 3.5 3.5L10 9l3 1 1 3-2 1.5C7 14 2 9 1.5 4z"/></svg>
        +61 7 3287 4419
      </li>
      <li>
        <svg viewBox="0 0 16 16" aria-hidden="true"><rect x="4" y="1.5" width="8" height="13" rx="1.5"/><path d="M7 12.3h2"/></svg>
        0471 352 608
      </li>
      <li>
        <svg viewBox="0 0 16 16" aria-hidden="true"><rect x="1.5" y="3.5" width="13" height="9"/><path d="M1.5 3.5L8 9l6.5-5.5"/></svg>
        marcus@quillbrookcapital.com.au
      </li>
      <li>
        <svg viewBox="0 0 16 16" aria-hidden="true"><circle cx="8" cy="8" r="6.3"/><path d="M1.7 8h12.6M8 1.7c-3 3.5-3 9 0 12.6M8 1.7c3 3.5 3 9 0 12.6"/></svg>
        www.quillbrookcapital.com.au
      </li>
    </ul>
    <p class="address">Level 36 Tindale Court, 58 Harwick St Brisbane QLD 4000</p>
    <div class="foil-stripe"></div>
  </section>
</body>
</html>
```